Wordpress Design ProjectWP website design (Vosberg)

We need a wordpress design that will incorporate a professional color scheme with company logo in a clean layout. The design needs to consider that this will be developed on a responsive theme. Colors are undetermined - use a colors in logo - maybe a light color, maybe yellow accent, and black. Client wants a 'modern' look.

Industry/Entity Type

It Company

Font styles to use
Serif
Sans Serif

Requirements
Must have
• Navigation: 1) Home 2) Auctions 3) Services 4) About Us 5) Contact us
• Site will have a slideshow element (initial image attached) and the following widgets: 1)Social Media (facebook,RSS) 2) Email Sign Up Form 3) Featured Video, 4) Auction Search
• Homepage content: "Vosberg Auction & Real Estate
• Since 1958 We at Vosberg Auction & Real Estate have offered our services to our clients as a versatile Auction Company with the ability to perform a variety of Auction types.
• Having sold Items such as: Real Estate, Machinery, Antiques, Tools, and much, more; we have constructed a strong foundation of knowledge and experience of the appropriate Auction marketing and preparation logistics. This results in a high quality Auction service that we provide to our clients, and also a level of service that we take great pride in.
• When you are ready for your Auction, you want it done right!
• Call Us at Vosberg Auction & Real Estate,"
• In the footer, there will be smaller company logo, the affiliations logo (attached), and contact info below:
• Vosberg Auction, Inc.
• 4135 County Highway 82
• Cedar Hollow, NY 13921
• 555-010-0143
Nice to have
• Use of a dropdown menu with styling.

```html
<!DOCTYPE html>
<html lang="en">
<head>
<meta charset="utf-8">
<title>Vosberg Auction &amp; Real Estate</title>
<link href="https://fonts.googleapis.com/css2?family=Roboto:wght@300;400;500;700&display=swap" rel="stylesheet">
<style>
:root{
  --navy:#16173f;
  --yellow:#ffde00;
  --gray-bg:#efefef;
  --frame:#e4e4e4;
  --text:#333;
  --muted:#888;
  --line:#cfcfcf;
  --white:#fff;
}
*{box-sizing:border-box;margin:0;padding:0}
html,body{width:1200px;height:1161px;overflow:hidden;background:var(--white);font-family:'Roboto',sans-serif;color:var(--text)}
.page{position:relative;width:1200px;height:1161px}
.abs{position:absolute}

.brand{left:299px;top:32px;width:114px;height:58px;display:flex;align-items:center;gap:6px}
.brand-mark{width:12px;height:12px;background:var(--navy);flex:none}
.brand-name{font-size:26px;font-weight:700;color:var(--navy);letter-spacing:-.5px;white-space:nowrap}

.main-nav{left:423px;top:56px;width:462px;height:34px;border-bottom:1px solid var(--line);display:flex;justify-content:flex-end}
.main-nav a{font-size:10px;color:#999;text-decoration:none;text-transform:uppercase;line-height:34px;margin-left:22px;white-space:nowrap}
.main-nav a.active{background:var(--navy);color:var(--white);font-weight:700;width:59px;text-align:center;border-bottom:4px solid var(--yellow);line-height:30px;margin-left:0}
.main-nav a:nth-child(2){margin-left:12px}

.social{left:299px;top:100px;display:flex;gap:4px}
.social span{width:26px;height:23px;background:var(--navy);display:block}

.search{left:681px;top:100px;width:204px;height:23px;display:flex}
.search input{flex:1;min-width:0;border:1px solid #ddd;border-right:0;font:400 7px 'Roboto',sans-serif;padding-left:9px;color:#aaa;text-transform:uppercase;outline:none}
.search button{width:29px;border:0;background:var(--navy);display:flex;align-items:center;justify-content:center}

.gray-area{left:0;top:353px;width:1200px;height:332px;background:var(--gray-bg)}
.band{left:0;top:173px;width:1200px;height:180px;background:var(--yellow)}
.slider-frame{left:232px;top:137px;width:719px;height:248px;background:var(--frame)}
.slider-shadow{left:265px;top:382px;width:653px;height:14px;border-radius:50%;box-shadow:0 6px 8px -4px rgba(0,0,0,.35)}
.slide{left:239px;top:145px;width:703px;height:234px;background:linear-gradient(180deg,#6f6a5e 0%,#5b6a58 45%,#4b4f5a 100%)}
.dots{left:570px;top:362px;display:flex;gap:4px}
.dots i{width:8px;height:8px;border-radius:50%;background:var(--white);display:block}
.dots i:first-child{background:var(--yellow)}

.center{left:0;width:1200px;text-align:center}
.h-title{font-size:19px;font-weight:400;color:#333}
.h-sub{font-size:15px;font-weight:300;color:#444}
.copy{font-size:9.5px;line-height:14.5px;color:#666}

.videos{left:299px;top:546px;display:flex;gap:8px}
.video{width:141px;height:84px;border-bottom:4px solid var(--navy);position:relative}
.video.active{border-bottom-color:var(--yellow)}
.v1{background:linear-gradient(135deg,#2a2a2a,#b3232b)}
.v2{background:linear-gradient(180deg,#8a9aa8,#5a5550)}
.v3{background:linear-gradient(135deg,#e9e4de,#9aa3b5)}
.v4{background:linear-gradient(135deg,#f2f2f2,#d4d4d4 60%,#7a5a2a)}
.play{position:absolute;left:57px;top:25px}
.link{font-size:9.5px;color:#555;text-decoration:underline}

.tabs{left:299px;top:751px;width:134px}
.tabs li{list-style:none;font-size:9.5px;color:#888;height:24.5px;line-height:20px;border-bottom:1px solid #ddd}
.tabs li.active{color:var(--navy);border-bottom:2px solid var(--navy)}
.view-all{left:820px;top:754px;width:65px;text-align:right;font-size:9.5px;color:#999}
.sold{top:773px;width:212px;height:96px}
.s1{left:448px;background:linear-gradient(180deg,#4d6a3a,#8f8270 60%,#6a7a45)}
.s2{left:673px;background:linear-gradient(180deg,#8a7a6a,#3a3a3a 60%,#b8683a)}

.cta{left:0;top:959px;width:1200px;height:71px;background:var(--navy);color:var(--white);text-align:center}
.cta-line1{position:absolute;left:0;width:100%;top:17px;font-size:10px}
.cta-rule{position:absolute;left:453px;top:37px;width:276px;height:1px;background:#8e8fa8}
.cta-line2{position:absolute;left:0;width:100%;top:44px;font-size:12px}

.signup{left:367px;top:1030px;width:451px;height:36px;background:var(--yellow);padding:5px 6px;display:flex;gap:6px}
.signup input{width:164px;height:25px;background:var(--white);border:0;font:400 9.5px 'Roboto',sans-serif;color:var(--yellow);padding-left:11px;outline:none}
.signup input::placeholder{color:#f2c400}
.signup button{flex:1;background:var(--navy);color:var(--yellow);border:0;font:700 9.5px 'Roboto',sans-serif}

.foot-brand{left:403px;top:1094px;width:96px;height:42px;display:flex;align-items:center;gap:4px}
.foot-brand .brand-mark{width:9px;height:9px}
.foot-brand .brand-name{font-size:19px}
.address{left:512px;top:1088px;font-size:8.5px;line-height:14.5px;color:#777;font-style:normal;white-space:nowrap}
.address strong{color:var(--navy);font-size:9px;font-weight:700}
.divider{left:642px;top:1094px;width:1px;height:44px;background:#ccc}
.badge-round{left:667px;top:1089px;width:70px;height:47px;border-radius:50%;border:2px solid #222}
.badge-square{left:749px;top:1093px;width:36px;height:40px;background:#222}
</style>
</head>
<body>
<div class="page">

  <div class="abs brand"><span class="brand-mark"></span><span class="brand-name">Vosberg</span></div>

  <nav class="abs main-nav">
    <a class="active" href="#">Home</a>
    <a href="#">Auctions</a>
    <a href="#">Services</a>
    <a href="#">About Us</a>
    <a href="#">Contact Us</a>
  </nav>

  <div class="abs social" aria-label="Social links">
    <span aria-label="Social profile 1"></span><span aria-label="Social profile 2"></span><span aria-label="Social profile 3"></span><span aria-label="News feed"></span>
  </div>

  <form class="abs search">
    <input type="text" placeholder="Search auctions">
    <button type="button" aria-label="Search">
      <svg width="13" height="13" viewBox="0 0 13 13"><circle cx="5" cy="5" r="3.6" fill="none" stroke="#fff" stroke-width="1.8"/><line x1="7.6" y1="7.6" x2="12" y2="12" stroke="#fff" stroke-width="2.2"/></svg>
    </button>
  </form>

  <div class="abs gray-area"></div>
  <div class="abs band"></div>
  <div class="abs slider-frame"></div>
  <div class="abs slider-shadow"></div>
  <div class="abs slide" role="img" aria-label="Crowd gathered around a green tractor at an outdoor auction"></div>
  <div class="abs dots"><i></i><i></i><i></i><i></i></div>

  <h1 class="abs center h-title" style="top:420px">Vosberg Auction &amp; Real Estate</h1>
  <p class="abs center copy" style="top:454px">Since 1958 We at Vosberg Auction &amp; Real Estate have offered our services to our clients as a versatile Auction Company<br>with the ability to perform a variety of Auction types.</p>

  <h2 class="abs center h-sub" style="top:510px">Featured Video</h2>
  <div class="abs videos">
    <div class="video v1" role="img" aria-label="Person beside a red auction banner"></div>
    <div class="video v2 active" role="img" aria-label="Crowd at an outdoor machinery auction">
      <svg class="play" width="26" height="26" viewBox="0 0 26 26"><circle cx="13" cy="13" r="12" fill="rgba(255,255,255,.7)"/><path d="M10 7.5 L18.5 13 L10 18.5Z" fill="#333"/></svg>
    </div>
    <div class="video v3" role="img" aria-label="Appraiser examining an antique vase"></div>
    <div class="video v4" role="img" aria-label="Auction gavel resting on a keyboard"></div>
  </div>
  <p class="abs center" style="top:650px"><a class="link" href="#">Find More</a></p>

  <h2 class="abs center h-sub" style="top:720px">Having Sold Items</h2>
  <ul class="abs tabs">
    <li class="active">Real Estate</li>
    <li>Machinery</li>
    <li>Antiques</li>
    <li>Tools</li>
    <li>Find More</li>
  </ul>
  <span class="abs view-all">+ View All</span>
  <div class="abs sold s1" role="img" aria-label="Single-storey brick house with a lawn and trees"></div>
  <div class="abs sold s2" role="img" aria-label="Group of buyers standing outside a brick house"></div>

  <p class="abs center copy" style="top:896px">We have constructed a strong foundation of knowledge and experience of the appropriate Auction marketing and preparation logistics.<br>This results in a high quality Auction service that we provide to our clients, and also a level of service that we take great pride in.</p>

  <section class="abs cta">
    <p class="cta-line1">When you are ready for your Auction, you want it done right!</p>
    <span class="cta-rule"></span>
    <p class="cta-line2">Call Us at Vosberg Auction &amp; Real Estate</p>
  </section>

  <form class="abs signup">
    <input type="text" placeholder="Your Name">
    <input type="email" placeholder="Your Email">
    <button type="button">SIGN UP</button>
  </form>

  <div class="abs foot-brand"><span class="brand-mark"></span><span class="brand-name">Vosberg</span></div>
  <address class="abs address">
    <strong>Vosberg Auction, Inc.</strong><br>
    4135 County Highway 82<br>
    Cedar Hollow, NY 13921<br>
    Call: 555-010-0143
  </address>
  <span class="abs divider"></span>
  <span class="abs badge-round" aria-label="State association badge"></span>
  <span class="abs badge-square" aria-label="National association badge"></span>

</div>
</body>
</html>
```